Postcard Design

Heating & Cooling

I want to create a post card for a Tune Up program that we offer customer for this spring.
Updates

I would like to change the date from April 1st - June 31st.
I would also like to change the size and go larger for the post card.

Keep the designs coming.
Thanks

I have decided to change the price of the cost of the program to "Only $99.00" due to other competitors pricing in my area.
If possible include at the bottom of the design > "Does not cover repair or parts" in a small font

Reason: We need more time for better designs. So I am extending the deadline by 7 days.

Target Market(s)

Residential Customers for Air Conditioning Tune Ups

Requirements
Must have
• We are promoting a tune up for the air conditioning system for $129.00.

The price is effective from April 1st - July 31st

I would like for the post card to be attention grabbing from the customers point of view. So mainly, add bold letting and everything to get attention.
Nice to have
• Also add to the card if possible:
Lower Energy Bills
Increase the life of your system
Prevent future breakdowns

Stay Cool this Summer with our Keystone Service Program

And add a logo that shows stacks of coins to indicate the money that can be saved

You also can look at other post cards that has been created for this particular program and design from it.

```html
<!DOCTYPE html>
<html lang="en">
<head>
<meta charset="utf-8">
<title>Summit Heating &amp; Cooling – Tune Up Postcard</title>
<link rel="stylesheet" href="https://fonts.googleapis.com/css2?family=Anton&family=Oswald:wght@400;500;700&display=swap">
<style>
  :root {
    --canvas: #f1f1f1;
    --sky: #3e9fd9;
    --crimson: #b8183a;
    --red: #e21d3a;
    --navy: #243a8f;
    --white: #ffffff;
    --green: #7cc142;
    --rule: #7a7ec4;
    --link-blue: #1f6fc0;
  }
  * { margin: 0; padding: 0; box-sizing: border-box; }
  html, body { width: 1200px; height: 1000px; overflow: hidden; }
  body { background: var(--canvas); position: relative; font-family: "Oswald", sans-serif; }

  .postcard { position: absolute; width: 544px; height: 421px; overflow: hidden; }
  .postcard--front { left: 106px; top: 55px; }
  .postcard--back { left: 576px; top: 500px; width: 548px; height: 422px; background: var(--white); border: 1px solid #dcdcdc; }

  .front-art { position: absolute; inset: 0; }

  .brand-box {
    position: absolute; left: 386px; top: 2px; width: 140px; height: 88px;
    background: var(--white); display: flex; align-items: center; justify-content: center; text-align: center;
  }
  .brand-name {
    font-family: "Oswald", sans-serif; font-weight: 700; color: var(--navy);
    font-size: 17px; line-height: 1.1; text-transform: uppercase;
  }

  .headline { position: absolute; left: 26px; width: 250px; text-align: center; white-space: nowrap; }
  .outlined { -webkit-text-stroke: 6px var(--white); paint-order: stroke fill; }
  .headline-summer {
    top: 38px; font-weight: 700; font-size: 25px;
    color: var(--red); letter-spacing: -0.3px; line-height: 1;
  }
  .headline-summer .cool { color: var(--navy); }
  .headline-program {
    top: 78px; font-weight: 700; font-size: 16px;
    color: var(--crimson); line-height: 1;
  }
  .headline-tuneup {
    top: 100px; width: auto; text-align: left; transform: scaleX(0.88); transform-origin: left top;
    font-family: "Anton", sans-serif; font-weight: 400; font-size: 88px; line-height: 1;
    color: var(--crimson);
  }
  .headline-system {
    top: 195px; font-weight: 700; font-size: 22px;
    color: var(--crimson); line-height: 1;
  }
  .headline-price {
    top: 220px; width: auto; text-align: left; transform: scaleX(0.86); transform-origin: left top;
    font-family: "Anton", sans-serif; font-size: 108px; line-height: 1;
    color: var(--red);
  }
  .price-dates {
    position: absolute; left: 24px; top: 332px; font-weight: 400;
    font-size: 13px; color: var(--red); white-space: nowrap;
    -webkit-text-stroke: 3px var(--white); paint-order: stroke fill;
  }
  .price-dates strong { font-weight: 700; font-size: 17px; }
  .disclaimer {
    position: absolute; left: 26px; width: 250px; top: 356px; text-align: right;
    font-size: 12px; color: var(--red); white-space: nowrap;
    -webkit-text-stroke: 3px var(--white); paint-order: stroke fill;
  }

  .benefit {
    position: absolute; left: 356px; height: 19px; background: var(--white);
    font-size: 11px; color: var(--link-blue);
    padding: 2px 0 0 12px; line-height: 15px; white-space: nowrap;
  }
  .benefit--energy { top: 248px; width: 118px; }
  .benefit--life { top: 269px; width: 150px; }
  .benefit--breakdowns { top: 294px; width: 130px; }

  .back-brand { position: absolute; left: 18px; top: 40px; }
  .back-brand .brand-name { font-size: 24px; }
  .stamp-box { position: absolute; left: 409px; top: 29px; width: 108px; height: 107px; border: 1px solid var(--rule); }
  .address-line { position: absolute; left: 294px; width: 222px; height: 0; border-top: 1px solid var(--rule); }
</style>
</head>
<body>

<section class="postcard postcard--front" aria-label="Postcard front">
  <svg class="front-art" width="544" height="421" viewBox="0 0 544 421">
    <defs>
      <linearGradient id="photoTone" x1="0" y1="0" x2="1" y2="1">
        <stop offset="0" stop-color="#8a4a3c"/>
        <stop offset="0.45" stop-color="#6c6f78"/>
        <stop offset="1" stop-color="#b9bcc0"/>
      </linearGradient>
    </defs>
    <rect class="band-red" width="544" height="421" fill="var(--crimson)"/>
    <path class="field-blue" d="M0,0 H300 C290,180 320,330 450,421 H140 C70,400 25,360 12,300 C5,200 4,100 0,30 Z" fill="var(--sky)"/>
    <path class="photo-area" role="img" aria-label="Photo: technician servicing an outdoor air conditioner unit beside a brick wall"
          d="M308,0 H544 V421 H488 C350,340 302,180 308,0 Z" fill="url(#photoTone)"/>
    <g class="savings-badge">
      <circle cx="316" cy="277" r="42" fill="var(--white)" stroke="var(--green)" stroke-width="5"/>
      <circle cx="316" cy="277" r="30" fill="#d9c27a" role="img" aria-label="Illustration: money bag with gold coins"/>
      <path d="M330,275 L345,292 L372,246" fill="none" stroke="var(--green)" stroke-width="6" stroke-linecap="round" stroke-linejoin="round"/>
    </g>
  </svg>

  <div class="brand-box"><span class="brand-name">Summit<br>Heating &amp; Cooling</span></div>

  <p class="headline headline-summer outlined">Stay <span class="cool">Cool</span> this Summer</p>
  <p class="headline headline-program outlined">with our Keystone Service Program</p>
  <h1 class="headline headline-tuneup outlined">TUNE UP</h1>
  <p class="headline headline-system outlined">AIR CONDITIONER SYSTEM</p>
  <p class="headline headline-price outlined">$99.00</p>
  <p class="price-dates">The price is effective from <strong>April 1st - July 31st</strong></p>
  <p class="disclaimer">Does not cover repair or parts*</p>

  <p class="benefit benefit--energy">Lower Energy Bills</p>
  <p class="benefit benefit--life">Increase the life of your system</p>
  <p class="benefit benefit--breakdowns">Prevent future breakdowns</p>
</section>

<section class="postcard postcard--back" aria-label="Postcard back">
  <div class="back-brand"><span class="brand-name">Summit<br>Heating &amp; Cooling</span></div>
  <div class="stamp-box"></div>
  <div class="address-line" style="top:195px"></div>
  <div class="address-line" style="top:220px"></div>
  <div class="address-line" style="top:260px"></div>
  <div class="address-line" style="top:285px"></div>
</section>

</body>
</html>
```